Vorential Health Posters

Two posters needed to introduce our new package pricing, called our SPARK and GLOW programs. Our current posters are attached, these two new posters should be similar design and layout. The docx attached has what information should be on each poster. (vorentialhealth.com)

```html
<!DOCTYPE html>
<html lang="en">
<head>
<meta charset="utf-8">
<title>Vorential Health – Package Posters</title>
<link href="https://fonts.googleapis.com/css2?family=Orbitron:wght@500;700;800&family=Exo+2:wght@800&family=Montserrat:ital,wght@0,400;0,700;1,400&display=swap" rel="stylesheet">
<style>
  :root {
    --stage: #e3e3e3;
    --red: #c1171d;
    --row: #262626;
    --ink: #111111;
    --white: #ffffff;
    --paper: #ffffff;
    --photo-top: #9a9a9a;
    --photo-mid: #4a4a4a;
    --photo-low: #2e2e2e;
  }
  * { box-sizing: border-box; margin: 0; padding: 0; }
  html, body { width: 1200px; height: 2746px; overflow: hidden; background: var(--stage); }
  .poster {
    position: absolute; left: 192px; width: 842px; height: 1262px;
    background: var(--paper);
    box-shadow: 0 10px 26px rgba(0,0,0,0.22);
  }
  .poster--glow { top: 66px; }
  .poster--spark { top: 1373px; }
  .hero {
    position: absolute; left: 0; top: 0; width: 842px; height: 1050px; overflow: hidden;
  }
  .hero__photo {
    position: absolute; inset: 0;
    background:
      radial-gradient(ellipse at 75% 30%, rgba(170,170,170,0.55), rgba(0,0,0,0) 55%),
      radial-gradient(ellipse at 85% 85%, rgba(120,120,120,0.45), rgba(0,0,0,0) 40%),
      linear-gradient(180deg, var(--photo-top) 0%, var(--photo-mid) 22%, var(--photo-low) 60%, #3a3a3a 100%);
  }
  .brand {
    position: absolute; top: 70px; left: 0; width: 100%; text-align: center;
    font-family: "Orbitron", sans-serif; font-weight: 700; font-size: 54px;
    letter-spacing: 2px; color: var(--red);
  }
  .title {
    position: absolute; top: 182px; left: 0; width: 100%; text-align: center;
    font-family: "Orbitron", sans-serif; font-weight: 800; font-size: 66px;
    letter-spacing: 2px; color: var(--white);
  }
  .tagline {
    position: absolute; top: 263px; left: 0; width: 100%; text-align: center;
    font-family: "Orbitron", sans-serif; font-weight: 500; font-size: 16px;
    letter-spacing: 0.5px; color: var(--white);
  }
  .benefits {
    position: absolute; top: 366px; left: 115px; width: 612px;
    display: flex; flex-direction: column; gap: 14px; list-style: none;
  }
  .benefit {
    position: relative; height: 81px; border-radius: 14px; background: var(--row);
    box-shadow: 0 3px 6px rgba(0,0,0,0.35);
  }
  .benefit__verb {
    position: absolute; left: 38px; top: 50%; transform: translateY(-50%);
    font-family: "Exo 2", sans-serif; font-weight: 800; font-size: 32px; color: var(--red);
  }
  .benefit__goal {
    position: absolute; left: 295px; top: 50%; transform: translateY(-50%);
    font-family: "Orbitron", sans-serif; font-weight: 700; font-size: 20px;
    color: var(--white); line-height: 1.2;
  }
  .poster--spark .benefit__goal { left: 398px; transform: translate(-50%, -50%); text-align: center; }
  .benefit__tick { position: absolute; right: 8px; top: 7px; width: 76px; height: 67px; }
  .powered {
    position: absolute; right: 0; bottom: 0; width: 375px; height: 103px;
  }
  .powered__shape { position: absolute; inset: 0; }
  .powered__small {
    position: absolute; left: 94px; top: 26px;
    font-family: "Montserrat", sans-serif; font-size: 21px; color: var(--white);
  }
  .powered__big {
    position: absolute; left: 94px; top: 52px;
    font-family: "Montserrat", sans-serif; font-size: 29px; letter-spacing: 0.5px; color: var(--white);
  }
  .offer {
    position: absolute; top: 1078px; left: 44px; width: 752px;
    display: flex; gap: 6px;
  }
  .offer__tag {
    height: 53px; width: 373px; display: flex; align-items: center; justify-content: center;
    font-family: "Montserrat", sans-serif; font-weight: 700; font-size: 25px; color: var(--white);
  }
  .offer__tag--price { background: var(--ink); }
  .offer__tag--save { background: var(--red); }
  .offer__note {
    position: absolute; top: 1143px; left: 0; width: 100%; text-align: center;
    font-family: "Montserrat", sans-serif; font-style: italic; font-size: 21px; color: var(--ink);
  }
</style>
</head>
<body>

<svg width="0" height="0" style="position:absolute">
  <defs>
    <symbol id="tick-box" viewBox="0 0 76 67">
      <rect x="3" y="3" width="70" height="61" rx="10" fill="none" stroke="#ffffff" stroke-width="4"/>
      <path d="M17 34 L31 50 L61 10" fill="none" stroke="#ffffff" stroke-width="7" stroke-linecap="round" stroke-linejoin="round"/>
    </symbol>
  </defs>
</svg>

<article class="poster poster--glow">
  <section class="hero">
    <div class="hero__photo" role="img" aria-label="Black and white photo of a muscular man lifting dumbbells in a gym"></div>
    <div class="brand">VORENTIAL</div>
    <h1 class="title">GLOW PACKAGE</h1>
    <p class="tagline">BURN FAT. BOOST ENERGY. TRANSFORM YOUR BODY.</p>
    <ul class="benefits">
      <li class="benefit"><span class="benefit__verb">INCREASE</span><span class="benefit__goal">FAT LOSS</span><svg class="benefit__tick"><use href="#tick-box"/></svg></li>
      <li class="benefit"><span class="benefit__verb">BOOST</span><span class="benefit__goal">METABOLISM</span><svg class="benefit__tick"><use href="#tick-box"/></svg></li>
      <li class="benefit"><span class="benefit__verb">IMPROVE</span><span class="benefit__goal">SLEEP</span><svg class="benefit__tick"><use href="#tick-box"/></svg></li>
      <li class="benefit"><span class="benefit__verb">PROTECT</span><span class="benefit__goal">MUSCLE MASS</span><svg class="benefit__tick"><use href="#tick-box"/></svg></li>
      <li class="benefit"><span class="benefit__verb">INCREASE</span><span class="benefit__goal">ENERGY</span><svg class="benefit__tick"><use href="#tick-box"/></svg></li>
    </ul>
    <div class="powered">
      <svg class="powered__shape" viewBox="0 0 375 103" preserveAspectRatio="none"><polygon points="55,0 375,0 375,103 0,103" fill="#c1171d"/></svg>
      <span class="powered__small">Powered by</span>
      <span class="powered__big">PEPTIDES + TRT</span>
    </div>
  </section>
  <div class="offer">
    <span class="offer__tag offer__tag--price">One Low Monthly Price</span>
    <span class="offer__tag offer__tag--save">Save BIG Over the Year</span>
  </div>
  <p class="offer__note">3 Months FREE When You Stay Committed All Year</p>
</article>

<article class="poster poster--spark">
  <section class="hero">
    <div class="hero__photo" role="img" aria-label="Black and white photo of a muscular man lifting dumbbells in a gym"></div>
    <div class="brand">VORENTIAL</div>
    <h1 class="title">SPARK PACKAGE</h1>
    <p class="tagline">GAIN MUSCLE. RECOVER FASTER. MAXIMIZE YOUR STRENGTH.</p>
    <ul class="benefits">
      <li class="benefit"><span class="benefit__verb">GAIN</span><span class="benefit__goal">MUSCLE MASS</span><svg class="benefit__tick"><use href="#tick-box"/></svg></li>
      <li class="benefit"><span class="benefit__verb">ACCELERATE</span><span class="benefit__goal">RECOVERY</span><svg class="benefit__tick"><use href="#tick-box"/></svg></li>
      <li class="benefit"><span class="benefit__verb">BOOST</span><span class="benefit__goal">STRENGTH</span><svg class="benefit__tick"><use href="#tick-box"/></svg></li>
      <li class="benefit"><span class="benefit__verb">IMPROVE</span><span class="benefit__goal">BODY<br>COMPOSITION</span><svg class="benefit__tick"><use href="#tick-box"/></svg></li>
      <li class="benefit"><span class="benefit__verb">INCREASE</span><span class="benefit__goal">ENERGY</span><svg class="benefit__tick"><use href="#tick-box"/></svg></li>
    </ul>
    <div class="powered">
      <svg class="powered__shape" viewBox="0 0 375 103" preserveAspectRatio="none"><polygon points="55,0 375,0 375,103 0,103" fill="#c1171d"/></svg>
      <span class="powered__small">Powered by</span>
      <span class="powered__big">PEPTIDES + TRT</span>
    </div>
  </section>
  <div class="offer">
    <span class="offer__tag offer__tag--price">One Low Monthly Price</span>
    <span class="offer__tag offer__tag--save">Save BIG Over the Year</span>
  </div>
  <p class="offer__note">3 Months FREE When You Stay Committed All Year</p>
</article>

</body>
</html>
```